Harwick Market
Your Authentic Market Experience
Project: Harwick Market
Harwick Market - Events
Creative Brief
Bright & Fun-filled
we will not be putting a name on the card
we will not be putting an address on the card
harwickmarketmanager@plovenmail.com
www.harwickfarmersmarket-example.com
Saturdays 2pm-4pm May long weekend - September long weekend
We haven't got a specific idea for the back of the card. We just know that we like the look of double sided cards
QJMDesignworks QJMDesignworks
DorvalTownStalls DorvalTownStalls

```html
<!DOCTYPE html>
<html lang="en">
<head>
<meta charset="utf-8">
<title>Harwick Market – Stationery</title>
<link rel="stylesheet" href="https://fonts.googleapis.com/css2?family=Montserrat:wght@400;500;600;700;800&display=swap">
<style>
  :root {
    --bg: #3b3b3b;
    --paper: #ffffff;
    --paper-soft: #f4f5ef;
    --green: #7b9b2f;
    --green-dark: #5f7d1f;
    --green-light: #b5cb63;
    --green-pale: #dfe8c2;
    --ink: #4a4a4a;
    --ink-soft: #8a8a8a;
  }
  * { box-sizing: border-box; margin: 0; padding: 0; }
  html, body { width: 1200px; height: 799px; overflow: hidden; }
  body {
    background: var(--bg);
    font-family: "Montserrat", Arial, sans-serif;
    color: var(--ink);
    position: relative;
  }

  .brand-name {
    font-family: "Montserrat", Arial, sans-serif;
    font-weight: 800;
    color: var(--green);
    display: flex;
    align-items: center;
    gap: 6px;
    line-height: 1;
    white-space: nowrap;
  }
  .brand-dot { width: 12px; height: 12px; border-radius: 50%; background: var(--green); flex: none; }

  .icon { width: 10px; height: 10px; flex: none; }
  .contact-line { display: flex; align-items: center; gap: 5px; white-space: nowrap; }

  /* Letterhead */
  .letterhead {
    position: absolute; left: 53px; top: 108px; width: 480px; height: 612px;
    background: var(--paper); overflow: hidden;
  }
  .letterhead .brand-name { position: absolute; left: 38px; top: 52px; font-size: 17px; }
  .letterhead .contact {
    position: absolute; right: 40px; top: 40px; font-size: 7px; color: var(--ink-soft);
    display: flex; flex-direction: column; gap: 4px;
  }
  .letterhead .contact .phone { font-size: 14px; font-weight: 700; color: var(--green-dark); }
  .letter-date { position: absolute; right: 40px; top: 118px; font-size: 7px; color: var(--ink-soft); }
  .letter-body {
    position: absolute; left: 38px; top: 148px; width: 390px;
    font-size: 7px; line-height: 1.75; color: var(--ink-soft);
  }
  .letter-body p { margin-bottom: 11px; }
  .letter-body .salutation { color: var(--ink); }
  .letter-sign { margin-top: 22px; }
  .letter-sign .name { color: var(--ink); margin-top: 20px; }
  .letter-arcs { position: absolute; left: 0; bottom: 0; width: 140px; height: 110px; }
  .letter-ornament {
    position: absolute; right: 40px; bottom: 30px; width: 66px; height: 66px;
    border-radius: 50%; background: var(--green-pale); opacity: .7;
  }

  /* Business card front */
  .card-front {
    position: absolute; left: 564px; top: 67px; width: 300px; height: 161px;
    background: var(--paper); border-radius: 8px; overflow: hidden;
  }
  .card-front .brand-name { position: absolute; left: 14px; top: 30px; font-size: 13px; gap: 5px; }
  .card-front .brand-dot { width: 10px; height: 10px; }
  .card-front .contact {
    position: absolute; left: 164px; top: 14px; font-size: 5.3px; color: var(--ink-soft);
    display: flex; flex-direction: column; gap: 4px;
  }
  .card-front .contact .phone { font-size: 11px; font-weight: 700; color: var(--green-dark); }
  .card-front .wave { position: absolute; left: 0; bottom: 0; width: 300px; height: 90px; }
  .card-front .schedule {
    position: absolute; left: 16px; bottom: 22px; color: var(--paper);
    display: flex; align-items: center; gap: 10px;
  }
  .card-front .schedule .day { font-size: 11px; font-weight: 700; }
  .card-front .schedule .hours { font-size: 5.5px; line-height: 1.4; font-weight: 500; }

  /* Business card back */
  .card-back {
    position: absolute; left: 564px; top: 240px; width: 300px; height: 156px;
    background: var(--paper); border-radius: 8px; overflow: hidden;
  }
  .card-back .tagline {
    position: absolute; left: 0; right: 0; top: 14px; text-align: center;
    font-size: 9px; font-weight: 600; color: var(--green-dark);
  }
  .card-back .scene {
    position: absolute; left: 0; bottom: 0; width: 300px; height: 122px;
    background: linear-gradient(180deg, var(--paper) 0%, var(--green-pale) 45%, var(--green-light) 100%);
  }

  /* Notebook */
  .notebook {
    position: absolute; left: 893px; top: 67px; width: 254px; height: 329px;
    border-radius: 18px; overflow: hidden;
    background: linear-gradient(160deg, var(--green-light), var(--green) 70%);
  }
  .notebook .title {
    position: absolute; left: 0; right: 0; top: 92px; text-align: center;
    color: var(--paper); font-weight: 800; line-height: .95;
  }
  .notebook .title .big { font-size: 46px; display: block; }
  .notebook .title .small { font-size: 24px; font-weight: 600; display: block; }
  .notebook .brand-name {
    position: absolute; right: 24px; bottom: 30px; font-size: 11px; color: var(--paper);
  }
  .notebook .brand-dot { background: var(--paper); width: 8px; height: 8px; }

  /* Envelope */
  .envelope {
    position: absolute; left: 564px; top: 492px; width: 583px; height: 240px;
    background: var(--paper); overflow: hidden;
  }
  .envelope .flap { position: absolute; left: 0; top: 0; width: 583px; height: 90px; }
  .envelope .contact {
    position: absolute; left: 16px; top: 28px; font-size: 6px; color: var(--ink-soft);
    display: flex; flex-direction: column; gap: 4px;
  }
  .envelope .contact .phone { font-size: 13px; font-weight: 700; color: var(--green-dark); }
  .envelope .brand-name { position: absolute; left: 300px; top: 38px; font-size: 17px; }
  .envelope .scene {
    position: absolute; left: 0; bottom: 0; width: 583px; height: 130px;
    background: linear-gradient(180deg, rgba(255,255,255,0) 0%, var(--paper-soft) 40%, #e3e6da 100%);
  }
</style>
</head>
<body>

  <section class="letterhead">
    <div class="brand-name"><span class="brand-dot"></span>Harwick Market</div>
    <div class="contact">
      <div class="contact-line phone">
        <svg class="icon" viewBox="0 0 10 10"><path d="M2 1h2l1 2-1.2 1a5 5 0 0 0 2.2 2.2L7 5l2 1v2a1 1 0 0 1-1 1A7 7 0 0 1 1 2a1 1 0 0 1 1-1z" fill="#5f7d1f"/></svg>
        403-555-0148
      </div>
      <div class="contact-line">harwickmarketmanager@plovenmail.com</div>
      <div class="contact-line">www.harwickfarmersmarket-example.com</div>
    </div>
    <div class="letter-date">November 1, 2021</div>
    <div class="letter-body">
      <p class="salutation">Dear Mr. Ellery,</p>
      <p>Thank you for joining our Saturday market season. Our vendors bring fresh produce, baked goods and local crafts to the square each week, and we are glad to count you among our friends and neighbours.</p>
      <p>This year we open on the May long weekend and close on the September long weekend. Stalls run from two until four each Saturday afternoon.</p>
      <p>Please confirm your stall size and power needs by the end of the month so we can plan the layout. Our team is happy to answer any questions you may have about set up or parking.</p>
      <p>We look forward to a bright and busy season together.</p>
      <div class="letter-sign">
        <div>Sincerely yours,</div>
        <div class="name">Your name</div>
        <div>Managing Director</div>
      </div>
    </div>
    <svg class="letter-arcs" viewBox="0 0 140 110" fill="none" stroke="#dfe8c2" stroke-width="5">
      <path d="M-10 110a80 80 0 0 1 160 0"/>
      <path d="M10 110a60 60 0 0 1 120 0"/>
      <path d="M30 110a40 40 0 0 1 80 0"/>
    </svg>
    <div class="letter-ornament" role="img" aria-label="Faint floral ornament"></div>
  </section>

  <section class="card-front">
    <div class="brand-name"><span class="brand-dot"></span>Harwick Market</div>
    <div class="contact">
      <div class="contact-line phone">
        <svg class="icon" viewBox="0 0 10 10"><path d="M2 1h2l1 2-1.2 1a5 5 0 0 0 2.2 2.2L7 5l2 1v2a1 1 0 0 1-1 1A7 7 0 0 1 1 2a1 1 0 0 1 1-1z" fill="#5f7d1f"/></svg>
        403-555-0148
      </div>
      <div class="contact-line">harwickmarketmanager@plovenmail.com</div>
      <div class="contact-line">www.harwickfarmersmarket-example.com</div>
    </div>
    <svg class="wave" viewBox="0 0 300 90" preserveAspectRatio="none">
      <path d="M0 30C80 5 180 5 300 24V90H0z" fill="#b5cb63"/>
      <path d="M0 42C90 18 190 18 300 36V90H0z" fill="#7b9b2f"/>
    </svg>
    <div class="schedule">
      <span class="day">Saturdays</span>
      <span class="hours">2pm - 4pm<br>May long weekend - September long weekend</span>
    </div>
  </section>

  <section class="card-back">
    <div class="tagline">Feeding your body and your soul</div>
    <div class="scene" role="img" aria-label="Illustration of a farmhouse, windmill and rolling green fields"></div>
  </section>

  <section class="notebook" role="img" aria-label="Notebook cover with green leaf pattern">
    <div class="title"><span class="big">Note</span><span class="small">Book</span></div>
    <div class="brand-name"><span class="brand-dot"></span>Harwick Market</div>
  </section>

  <section class="envelope">
    <svg class="flap" viewBox="0 0 583 90" fill="none">
      <path d="M0 0Q291 150 583 0" stroke="#e6e8e0" stroke-width="1.5"/>
    </svg>
    <div class="contact">
      <div class="contact-line phone">
        <svg class="icon" viewBox="0 0 10 10"><path d="M2 1h2l1 2-1.2 1a5 5 0 0 0 2.2 2.2L7 5l2 1v2a1 1 0 0 1-1 1A7 7 0 0 1 1 2a1 1 0 0 1 1-1z" fill="#5f7d1f"/></svg>
        403-555-0148
      </div>
      <div class="contact-line">harwickmarketmanager@plovenmail.com</div>
      <div class="contact-line">www.harwickfarmersmarket-example.com</div>
    </div>
    <div class="brand-name"><span class="brand-dot"></span>Harwick Market</div>
    <div class="scene" role="img" aria-label="Faint illustration of farmhouses, a windmill and a barn"></div>
  </section>

</body>
</html>
```